Business card for our large format printing and installation business

We want a professional looking business card for our business. We manufacture and install Signs.

On the back of the card add this info
Large Format Graphics Printing & Installations, Event Graphics, Banners, Posters, Vehicle Fleet Graphics, Boat Wraps, Wall Murals, Decals,Displays,Signs,Plaques,Digital Signs

On the Front of the card add the Tallowfern Signs logo, plus On the back of the card add the Orange Tallowfern Wraps logo. The 2 vector logos are attached to the design brief.

Target Market(s)

Local business owners

Contact Information for Business Card

Colors
f37122
f68d4e
f9ba93

Requirements
Must have
• On the Front of the card add the Tallowfern Signs logo, plus On the back of the card add the Orange Tallowfern Wraps logo. The 2 vector logos are attached to the design brief.

```html
<!DOCTYPE html>
<html lang="en">
<head>
<meta charset="utf-8">
<title>Tallowfern Signs – Business Card</title>
<link rel="stylesheet" href="https://fonts.googleapis.com/css2?family=Roboto:wght@400;500;700;900&display=swap">
<style>
  :root {
    --orange: #f37122;
    --orange-mid: #f68d4e;
    --orange-light: #f9ba93;
    --ink: #1c1c1c;
    --card-white: #f7f7f7;
    --card-dark: #1e1e1e;
    --card-dark-edge: #2b2b2b;
    --backdrop: #5f4c39;
    --text-light: #ffffff;
  }
  * { margin: 0; padding: 0; box-sizing: border-box; }
  html, body {
    width: 900px; height: 1200px; overflow: hidden;
    background: var(--backdrop);
    font-family: "Roboto", Arial, sans-serif;
  }
  .canvas { position: relative; width: 900px; height: 1200px; }

  .card {
    position: absolute; left: 66px; width: 780px; height: 430px;
    border-radius: 24px; overflow: hidden;
    box-shadow: 0 10px 28px rgba(0,0,0,.35);
  }

  /* Front */
  .card-front { top: 141px; background: var(--card-white); color: var(--ink); }
  .title-tab {
    position: absolute; left: 0; top: 45px; width: 159px; height: 60px;
    background: var(--ink); border-radius: 0 30px 30px 0;
    color: var(--orange); font-weight: 700; font-size: 30px;
    display: flex; align-items: center; justify-content: center;
  }
  .brand-front {
    position: absolute; right: 54px; top: 48px; text-align: right;
    color: var(--orange); font-weight: 900; line-height: .92;
    font-size: 64px; letter-spacing: -1px;
  }
  .person-name {
    position: absolute; left: 45px; top: 183px;
    font-size: 50px; font-weight: 700; line-height: 1; letter-spacing: .5px;
  }
  .address {
    position: absolute; left: 45px; top: 318px;
    font-size: 22px; line-height: 1.38; font-weight: 500;
  }
  .contact-list {
    position: absolute; left: 393px; top: 240px; list-style: none;
    font-size: 22px; font-weight: 500;
  }
  .contact-list li { display: flex; align-items: center; height: 33px; }
  .contact-list li.gap { margin-top: 27px; }
  .contact-list svg { width: 22px; height: 22px; margin-right: 14px; fill: var(--ink); flex: none; }

  /* Back */
  .card-back {
    top: 615px;
    background: radial-gradient(ellipse at 50% 40%, var(--card-dark-edge), var(--card-dark) 75%);
  }
  .brand-back {
    position: absolute; left: 0; right: 0; top: 72px; text-align: center;
    color: var(--orange); font-weight: 900; line-height: .92;
    font-size: 80px; letter-spacing: -1px;
  }
  .services {
    position: absolute; left: 40px; right: 40px; top: 285px;
    text-align: center; color: var(--text-light);
    font-size: 22px; font-weight: 700; line-height: 1.5;
  }
</style>
</head>
<body>
<div class="canvas">

  <section class="card card-front" aria-label="Business card front">
    <div class="title-tab">CEO</div>
    <div class="brand-front">Tallowfern<br>Signs</div>

    <h1 class="person-name">MARCO<br>DELVANE</h1>

    <p class="address">1480 Harbor Crest Lane #7<br>Brightwater, FL 30000</p>

    <ul class="contact-list">
      <li>
        <svg viewBox="0 0 24 24"><path d="M2 5h20v14H2z M4 7v.5l8 5.5 8-5.5V7z" fill-rule="evenodd"/></svg>
        Office:555-014-2280
      </li>
      <li>
        <svg viewBox="0 0 24 24"><path d="M6.6 10.8a15 15 0 0 0 6.6 6.6l2.2-2.2c.3-.3.7-.4 1-.2 1.1.4 2.3.6 3.6.6.6 0 1 .4 1 1V20c0 .6-.4 1-1 1C10.6 21 3 13.4 3 4c0-.6.4-1 1-1h3.5c.6 0 1 .4 1 1 0 1.3.2 2.5.6 3.6.1.3 0 .7-.2 1z"/></svg>
        Direct: 555-019-4731
      </li>
      <li class="gap">
        <svg viewBox="0 0 24 24"><path d="M3 8c0-2 2-4 9-4s9 2 9 4v2h-5V8H8v2H3z M5 12h14l2 8H3z"/></svg>
        Marco@tallowfern.net
      </li>
      <li>
        <svg viewBox="0 0 24 24"><path d="M7 2h10a1 1 0 0 1 1 1v18a1 1 0 0 1-1 1H7a1 1 0 0 1-1-1V3a1 1 0 0 1 1-1zm1 3v13h8V5z"/></svg>
        www.Tallowfernwraps.com
      </li>
    </ul>
  </section>

  <section class="card card-back" aria-label="Business card back">
    <div class="brand-back">Tallowfern<br>Wraps</div>
    <p class="services">Large Format Graphics Printing &amp; Installations, Event Graphics, Banners, Posters, Vehicle Fleet Graphics, Boat Wraps, Wall Murals, Decals, Displays, Signs, Plaques, Digital Signs</p>
  </section>

</div>
</body>
</html>
```